Serial Entrepreneur Business Card: 4 Logo Design

I am a serial entrepreneur and a full time mechanical engineer. I have four businesses. I would like to display them all on one business card.
*Please see the attached PDF for the design requirements*

www.KelbroNest.com

Businesses
-KelbroNest
-Quiet Lantern Properties
-Torlen Products
-Drosk Harbor Cast

Target Market(s)

Clients, Entrepreneurs, Associates, really anyone. Should be very professional.

Industry/Entity Type

Entrepreneur

Contact Information for Business Card

3.5" x 2" Standard Business Card Size
** Please review the attached requirement PDF for in depth detail on what I am expecting**

Font styles to use
Sans Serif

Requirements
Must have
• My personal contact information:
• First Name: Dae hwan
• Last Name: Pellow
• Nick Name: Riko
• Address: 83 Tolmer Court, Garfield NJ 07392
• Phone Number: 201-574-2916
• Email: RikodPellow@mailnest.example
• Website: www.KelbroNest.com
• All Four Logos of the Companies I own:
• -KelbroNest
• -Quiet Lantern Properties
• -Torlen Products
• -Drosk Harbor Cast
• My Professions:
• -Prototyping Engineer
• -Real Estate Investor
• -Financial Blogger
• -Video Podcaster
• -Online Retail Seller
Nice to have
• If it fits, please include the website for each logo, if there is more space please include the email for each.
• It might be nice to have the QX GUILD Logo, or TOVRA logo for my full-time job. But only if it fits.

```html
<!DOCTYPE html>
<html lang="en">
<head>
<meta charset="utf-8">
<title>KelbroNest Business Card</title>
<link href="https://fonts.googleapis.com/css2?family=Open+Sans:wght@400;600;700&display=swap" rel="stylesheet">
<style>
  :root {
    --backdrop: #5e4b3c;
    --card-white: #ffffff;
    --brand-green: #0c870c;
    --bright-green: #22a322;
    --ink: #1a1a1a;
    --muted: #555555;
    --divider: #b5b5b5;
    --band-black: #0a0a0a;
  }
  * { box-sizing: border-box; margin: 0; padding: 0; }
  html, body {
    width: 1200px; height: 987px; overflow: hidden;
    background: var(--backdrop);
    font-family: "Open Sans", sans-serif;
  }
  .canvas { position: relative; width: 1200px; height: 987px; }
  .card {
    position: absolute; left: 293px; width: 615px; height: 352px;
    border-radius: 19px; overflow: hidden;
  }
  .card--front { top: 130px; background: var(--card-white); display: flex; }
  .card--back { top: 505px; background: var(--brand-green); color: #fff; }

  /* front */
  .primary-brand {
    width: 319px; border-right: 1px solid var(--divider);
    display: flex; flex-direction: column; align-items: center; justify-content: center;
    padding-top: 90px;
  }
  .brand-name { display: flex; align-items: center; gap: 8px; font-weight: 700; color: var(--ink); }
  .brand-mark { width: 14px; height: 14px; border-radius: 50%; background: var(--bright-green); }
  .primary-brand .brand-name { font-size: 40px; letter-spacing: -0.5px; }
  .primary-brand .brand-mark { width: 20px; height: 20px; }
  .brand-url { font-size: 13px; letter-spacing: 3.2px; color: var(--muted); margin-top: 2px; }
  .ventures { flex: 1; display: flex; flex-direction: column; }
  .venture {
    display: flex; flex-direction: column; align-items: center; justify-content: center;
    border-bottom: 1px solid var(--divider);
  }
  .venture:last-child { border-bottom: none; }
  .venture--cast { height: 124px; padding-top: 18px; }
  .venture--properties { height: 94px; }
  .venture--products { flex: 1; padding-top: 20px; }
  .venture .brand-name { font-size: 22px; }
  .venture--cast .brand-name { color: var(--brand-green); }
  .venture .brand-url { font-size: 11px; letter-spacing: 2px; }

  /* back */
  .brand-row {
    position: absolute; top: 58px; left: 0; right: 0;
    display: flex; justify-content: center; gap: 18px;
    font-size: 13px; font-weight: 700; letter-spacing: 0.3px;
  }
  .rule {
    position: absolute; left: 120px; right: 120px; height: 1px;
    background: linear-gradient(90deg, transparent, rgba(255,255,255,0.45), transparent);
  }
  .rule--top { top: 118px; }
  .rule--bottom { top: 210px; }
  .owner { position: absolute; top: 126px; left: 0; right: 0; text-align: center; }
  .owner-name { font-size: 24px; font-weight: 700; line-height: 1.2; }
  .owner-roles { font-size: 15px; line-height: 1.4; }
  .contact { position: absolute; top: 218px; left: 0; right: 0; text-align: center; font-size: 15px; line-height: 1.6; }
  .contact b { font-weight: 700; }
  .growth-band { position: absolute; left: 0; bottom: 0; width: 615px; height: 70px; }
  .band-url {
    position: absolute; right: 24px; bottom: 6px;
    font-size: 15px; font-weight: 700; letter-spacing: 3px; color: #fff;
  }
</style>
</head>
<body>
<main class="canvas">
  <section class="card card--front">
    <div class="primary-brand">
      <div class="brand-name"><span class="brand-mark"></span>KelbroNest</div>
      <div class="brand-url">www.KelbroNest.com</div>
    </div>
    <div class="ventures">
      <div class="venture venture--cast">
        <div class="brand-name">Drosk Harbor Cast</div>
        <div class="brand-url">www.droskharborcast.com</div>
      </div>
      <div class="venture venture--properties">
        <div class="brand-name">Quiet Lantern Properties</div>
        <div class="brand-url">www.quietlantern.com</div>
      </div>
      <div class="venture venture--products">
        <div class="brand-name">Torlen Products</div>
        <div class="brand-url">www.torlen.com</div>
      </div>
    </div>
  </section>

  <section class="card card--back">
    <div class="brand-row">
      <span>KelbroNest</span><span>Torlen</span><span>Quiet Lantern</span><span>Drosk Harbor</span>
    </div>
    <div class="rule rule--top"></div>
    <div class="owner">
      <div class="owner-name">Dae hwan Pellow</div>
      <div class="owner-roles">Prototyping Engineer | Real Estate Investor | Financial Blogger<br>Video Podcaster | Online Retail Seller</div>
    </div>
    <div class="rule rule--bottom"></div>
    <div class="contact">
      83 Tolmer Court, Garfield NJ 07392<br>
      <b>P:</b> 201-574-2916 <b>E:</b> RikodPellow@mailnest.example
    </div>
    <svg class="growth-band" viewBox="0 0 615 70" aria-hidden="true">
      <polygon points="0,62 316,62 352,34 615,34 615,70 0,70" fill="var(--band-black)"/>
      <polygon points="0,50 310,50 350,20 343,12 370,8 362,34 355,27 316,58 0,58" fill="#ffffff"/>
    </svg>
    <div class="band-url">www.KelbroNest.com</div>
  </section>
</main>
</body>
</html>
```